B.L.W.T. Business Card Design

we need a business card design for a motor vehicle repair business in Southport Australia, called Dravo's Automotive Repair Services. Our services include panel & paint, resprays and light bodyworks. We have a logo which we would like to use on the business card. We would like to see designs that use the colours blue and grey.

Industry/Entity Type

Automotive

Contact Information for Business Card

Dravo's Automotive Repair Services,
Merrin Folke,
7/2-5 Tralby Street Wendlow 4290, 0468 732 180, /dravosautomotiverepairservices, dravosautomotiverepairservices@quellmail.example,
services: panel & paint, respray, light bodyworks.
ABN: 47 206 519 782

Requirements
Must have
• Front of card must include attached logo and contact details.
please list services
Your eye should be drawn to the name (Merrin Folke) and phone number (0468 732 180).
Font must be legible and contemporary.
back of business card should have the following:
1. title - quote and
2. list the following: for, date, valid till, quote details and
3. a footer "to book you repair, please contact Merrin Folke on 0468 732 180".
There needs to be enough space to hand write details.
Should not have
• do not include any graphics/illustrations.

```html
<!DOCTYPE html>
<html lang="en">
<head>
<meta charset="utf-8">
<title>B.L.W.T. Business Card Design</title>
<link rel="stylesheet" href="https://fonts.googleapis.com/css2?family=Lato:wght@400;700;900&display=swap">
<style>
  :root {
    --brand-blue: #1b86c8;
    --brand-blue-dark: #1570ad;
    --ink: #1d1d1f;
    --rule: #8a8f95;
    --paper: #ffffff;
    --backdrop: #d9dcdf;
  }
  * { box-sizing: border-box; margin: 0; padding: 0; }
  html, body {
    width: 1200px; height: 926px; overflow: hidden;
    background: var(--backdrop);
    font-family: "Lato", Arial, sans-serif;
  }
  .sheet {
    position: relative; width: 1200px; height: 926px;
    display: flex; flex-direction: column; align-items: center;
    justify-content: space-evenly;
  }
  .card {
    position: relative; width: 680px; height: 416px; overflow: hidden;
    box-shadow: 0 4px 14px rgba(0,0,0,.18);
  }

  /* ---------- Back of card ---------- */
  .card-back { background: var(--brand-blue); }
  .quote-panel {
    position: absolute; left: 30px; right: 30px; top: 26px; height: 262px;
    background: var(--paper); padding: 18px 34px 0;
  }
  .brand-name {
    display: flex; align-items: center; gap: 10px;
    color: var(--brand-blue); font-weight: 900; text-transform: uppercase;
    line-height: 1.05;
  }
  .brand-name .brand-dot {
    width: 14px; height: 14px; border-radius: 50%; background: var(--brand-blue); flex: none;
  }
  .quote-panel .brand-name { justify-content: center; font-size: 19px; margin-bottom: 18px; }
  .quote-field {
    display: flex; align-items: flex-end; gap: 8px;
    font-size: 14px; color: var(--ink); text-transform: uppercase;
    height: 32px;
  }
  .quote-field .write-line { flex: 1; border-bottom: 1px solid var(--rule); height: 1px; margin-bottom: 4px; }
  .quote-field .label-gap { margin-left: 14px; }
  .blank-line { height: 32px; border-bottom: 1px solid var(--rule); }
  .booking-note {
    position: absolute; left: 0; right: 0; top: 306px;
    text-align: center; color: var(--paper); font-size: 19px; line-height: 1.4;
  }
  .booking-note .booking-title { text-transform: uppercase; }
  .booking-note strong { font-weight: 900; }

  /* ---------- Front of card ---------- */
  .card-front { background: var(--paper); }
  .card-front .brand-name {
    position: absolute; left: 34px; top: 44px; font-size: 24px; width: 300px;
  }
  .contact-person {
    position: absolute; right: 34px; top: 134px; text-align: right;
  }
  .person-name {
    font-size: 30px; letter-spacing: 1px; text-transform: uppercase; color: var(--brand-blue);
  }
  .person-name .surname { font-weight: 900; color: var(--brand-blue-dark); }
  .person-phone {
    display: flex; align-items: center; justify-content: flex-end; gap: 8px;
    font-size: 23px; font-weight: 900; color: var(--ink); letter-spacing: 1px; margin-top: 2px;
  }
  .person-phone svg { width: 20px; height: 20px; }
  .edge-tab {
    position: absolute; right: 0; top: 142px; width: 14px; height: 46px; background: var(--brand-blue);
  }
  .contact-lines {
    position: absolute; left: 34px; right: 34px; top: 206px;
    font-size: 15px; line-height: 1.35; color: var(--ink);
  }
  .contact-lines .tag { color: var(--brand-blue); font-weight: 700; }
  .contact-lines .right-block { text-align: right; margin-top: 4px; }
  .service-band {
    position: absolute; left: 0; right: 0; top: 316px; bottom: 0;
    background: var(--brand-blue); color: var(--paper); text-align: center; padding-top: 16px;
  }
  .service-band h2 { font-size: 24px; font-weight: 400; letter-spacing: 2px; text-transform: uppercase; }
  .service-list { font-size: 19px; letter-spacing: 3px; text-transform: uppercase; margin-top: 10px; }
</style>
</head>
<body>
<main class="sheet">

  <section class="card card-back" aria-label="Back of business card">
    <div class="quote-panel">
      <div class="brand-name"><span class="brand-dot"></span>Dravo's Automotive Repair Services</div>
      <div class="quote-field"><span>Date</span><span class="write-line" style="flex:0 0 190px"></span></div>
      <div class="quote-field"><span>Quote details</span><span class="write-line"></span><span class="label-gap">Valid till</span><span class="write-line"></span></div>
      <div class="blank-line"></div>
      <div class="blank-line"></div>
    </div>
    <p class="booking-note">
      <span class="booking-title">To book you repair</span><br>
      Please contact <strong>Merrin Folke</strong> on <strong>0468 732 180</strong>
    </p>
  </section>

  <section class="card card-front" aria-label="Front of business card">
    <div class="brand-name"><span class="brand-dot"></span>Dravo's Automotive Repair Services</div>

    <div class="contact-person">
      <p class="person-name">Merrin <span class="surname">Folke</span></p>
      <p class="person-phone">
        <svg viewBox="0 0 24 24" aria-hidden="true"><path fill="#1d1d1f" d="M6.6 10.8a15.2 15.2 0 0 0 6.6 6.6l2.2-2.2a1 1 0 0 1 1-.25 11.4 11.4 0 0 0 3.6.57 1 1 0 0 1 1 1V20a1 1 0 0 1-1 1A17 17 0 0 1 3 4a1 1 0 0 1 1-1h3.5a1 1 0 0 1 1 1c0 1.25.2 2.46.57 3.6a1 1 0 0 1-.25 1z"/></svg>
        0468 732 180
      </p>
    </div>
    <div class="edge-tab"></div>

    <div class="contact-lines">
      <p><span class="tag">email:</span> dravosautomotiverepairservices@quellmail.example</p>
      <p><span class="tag">add:</span> Dravo's Automotive Repair Services,</p>
      <div class="right-block">
        <p><span class="tag">ABN:</span> 47 206 519 782</p>
        <p>7/2-5 Tralby Street Wendlow 4290</p>
      </div>
    </div>

    <div class="service-band">
      <h2>Services</h2>
      <p class="service-list">Panel &amp; Paint, Respray, Light Bodyworks</p>
    </div>
  </section>

</main>
</body>
</html>
```